New website

We ned to create a new website that reflects more who we are. We are delivering exclusive premium products to our customers and the current website does not reflect our products at all.
We believe in less is more and need a webpage that is clean yet professional and exclusive.

Target Market(s)

Dentistry

Industry/Entity Type

Dental

Number of Pages Required

5+ page

Font styles to use
Sans Serif

Colors

Designer to choose colors to be used in the design.

Requirements
Must have
• Picture gallery
• Nice structure
• Clean layout
Nice to have
• Light fonts
Should not have
• Any italic font styles

```html
<!DOCTYPE html>
<html lang="en">
<head>
<meta charset="utf-8">
<title>Lumora – Shade Analysis</title>
<link rel="stylesheet" href="https://fonts.googleapis.com/css2?family=Montserrat:wght@600;700&family=Roboto:wght@300;400&display=swap">
<style>
  :root {
    --teal: #2ad8d2;
    --teal-deep: #1fb6b9;
    --teal-shadow: #1a8f95;
    --coral: #ec5d5a;
    --heading-red: #e85a55;
    --ink: #555a5e;
    --nav-active: #20484f;
    --link: #25b3d6;
    --white: #ffffff;
    --lang-active: #e8334f;
  }
  * { margin: 0; padding: 0; box-sizing: border-box; }
  html, body { width: 1200px; height: 982px; overflow: hidden; background: var(--white); }
  body { position: relative; font-family: "Roboto", sans-serif; color: var(--ink); }

  .hero {
    position: absolute; left: 0; top: 0; width: 1200px; height: 395px;
    overflow: hidden;
  }
  .hero-photo {
    position: absolute; inset: 0;
    background:
      radial-gradient(ellipse 420px 380px at 860px 170px, rgba(60,120,120,0.45), rgba(0,0,0,0) 70%),
      linear-gradient(90deg, var(--teal) 0%, var(--teal) 45%, var(--teal-deep) 75%, var(--teal-shadow) 100%);
  }
  .brand {
    position: absolute; left: 46px; top: 68px;
    display: flex; align-items: center; gap: 10px;
    color: var(--white);
  }
  .brand-square { width: 12px; height: 12px; background: var(--white); }
  .brand-name {
    font-family: "Roboto", sans-serif; font-weight: 300; font-size: 20px;
    letter-spacing: 3px;
  }
  .main-nav {
    position: absolute; left: 288px; top: 77px;
    display: flex; gap: 18px;
    font-family: "Montserrat", sans-serif; font-weight: 600; font-size: 11.5px;
    letter-spacing: 0.5px; color: var(--white);
  }
  .main-nav a { color: inherit; text-decoration: none; }
  .main-nav .is-active { color: var(--nav-active); }
  .lang-switch {
    position: absolute; right: 44px; top: 40px;
    font-family: "Montserrat", sans-serif; font-weight: 600; font-size: 9px; color: var(--white);
  }
  .lang-switch .is-active { color: var(--lang-active); }
  .hero-title {
    position: absolute; left: 102px; top: 217px;
    font-family: "Montserrat", sans-serif; font-weight: 700; font-size: 42px;
    letter-spacing: 3px; color: var(--white);
  }

  .content { position: absolute; left: 102px; top: 446px; width: 678px; }
  .section-title {
    font-family: "Montserrat", sans-serif; font-weight: 700; font-size: 25px;
    letter-spacing: 2.5px; color: var(--heading-red); margin-bottom: 10px;
  }
  .content p { font-weight: 300; font-size: 13.2px; line-height: 19.5px; margin-bottom: 19.5px; }
  .content a { color: var(--link); text-decoration: underline; text-decoration-thickness: 1px; }

  .side-photo {
    position: absolute; left: 782px; top: 494px; width: 316px; height: 319px;
    background: linear-gradient(135deg, #ffffff 0%, #f1ece8 40%, #e9d3c6 70%, #f4f1ee 100%);
  }

  .site-footer {
    position: absolute; left: 0; top: 892px; width: 1200px; height: 90px;
    background: var(--coral); color: var(--white);
    display: flex; align-items: center; justify-content: center;
    font-family: "Roboto", sans-serif; font-size: 10px; font-weight: 400;
  }
</style>
</head>
<body>
  <header class="hero">
    <div class="hero-photo" role="img" aria-label="Close-up photo of a smiling patient in teal tones"></div>
    <div class="brand">
      <span class="brand-square"></span>
      <span class="brand-name">LUMORA</span>
    </div>
    <nav class="main-nav">
      <a href="#">WELCOME</a>
      <a href="#">PRODUCTS</a>
      <a href="#">SPECIAL SERVICES</a>
      <a href="#">SMILE GALLERY</a>
      <a href="#">THE COMPANY</a>
      <a href="#" class="is-active">SHADE ANALYSIS</a>
      <a href="#">CONTACT</a>
    </nav>
    <div class="lang-switch"><span class="is-active">ENG</span> | SWE</div>
    <h1 class="hero-title">SHADE ANALYSIS</h1>
  </header>

  <main class="content">
    <h2 class="section-title">SHADE ANALYSIS</h2>
    <p>Another tool is made by Veradent and is called TonePilot read more about it <a href="#">here&gt;&gt;</a><br>
    About 80% of the patients are aware of differences which will arise between their natural teeth and restorations made for them. So the dental surgeons need a system of accurate and exact choice of colors which can guarantee the perfectly adapted shade of artificial teeth.</p>
    <p>There are lot of shade guides available for us in this respect. So which guide is to bvte chosen? As dental technicians we use burnt porcelain samples, processed in laboratory with 100% accuracy. This should be the most exact way of a color choice. However, in order to spare time and to increase the exactness of the choice, Corta has developed a three-dimensional system adapted for full guide of colors of natural teeth. It will help you, the dental surgeons, to chose quickly a proper, basic color of teeth. This system is called Cortapan 3-D GUIDE.</p>
    <p>The ceramics used at Lumora being perfectly adapted to the shade guide, the teeth color will always be exactly the same as this, ordered by you. If you want to borrow a video cassette or inter-active CD-ROM, or obtain more information on this system, don't hesitate to address your inquiries to us or to take a look at the homepage of <a href="#">Corident</a></p>
    <p>To make your life easier you can get some help from Hue-scan, a digital shade taking tool from Lumetric. You can also easily communicate with us using Hue-scan. Read more: <a href="#">www.huescan.com</a></p>
  </main>

  <div class="side-photo" role="img" aria-label="Photo of a patient having tooth shade measured with a handheld device"></div>

  <footer class="site-footer">
    Lumora AB &nbsp;-&nbsp; Box 5120 &nbsp;-&nbsp; 53380 Lindvik, Sverige &nbsp;-&nbsp; Tel: +46-31-12 34 56
  </footer>
</body>
</html>
```